Business Cards and Stationery TQ5
TQ5 is the Umbrella company for a number of different smaller companies.
Business Cards and Stationery TQ5  - Directories
Creative Brief
Professional
Pieter de Wolff
Lindelaantje 417 Postbus 64 1937 RT Lindemeer Netherlands
Pieter.Wolff@tq5.nl
www.TQ5.nl
We would like a 'professional' basic layout with the logo present. A simple white background. A part of the logo can be uses as as watermark (grayed out)
Directories

```html
<!DOCTYPE html>
<html lang="nl">
<head>
<meta charset="utf-8">
<title>TQ5 – Business Cards</title>
<link href="https://fonts.googleapis.com/css2?family=Didact+Gothic&display=swap" rel="stylesheet">
<style>
  :root {
    --backdrop: #ecebe8;
    --card: #ffffff;
    --purple: #6a2a6c;
    --purple-deep: #4a1650;
    --purple-light: #8e4a8f;
    --grey-dark: #3a3a3a;
    --grey: #7b7b7b;
    --grey-light: #d9d9d9;
    --ink: #222222;
  }
  * { margin: 0; padding: 0; box-sizing: border-box; }
  html, body { width: 1200px; height: 427px; overflow: hidden; }
  body {
    background: var(--backdrop);
    font-family: "Didact Gothic", sans-serif;
    color: var(--ink);
    position: relative;
  }
  .card {
    position: absolute;
    top: 60px;
    width: 540px;
    height: 296px;
    background: var(--card);
    box-shadow: 0 3px 10px rgba(0,0,0,0.18);
    overflow: hidden;
  }
  .card--front { left: 43px; }
  .card--back { left: 636px; }

  .brand {
    position: absolute;
    left: 0; right: 0;
    display: flex;
    align-items: center;
    justify-content: center;
    gap: 12px;
    color: var(--purple);
    line-height: 1;
  }
  .brand__dot { border-radius: 50%; background: var(--purple); }
  .card--front .brand { top: 38px; }
  .card--front .brand__name { font-size: 70px; letter-spacing: 2px; }
  .card--front .brand__dot { width: 32px; height: 32px; }
  .card--back .brand { top: 62px; }
  .card--back .brand__name { font-size: 92px; letter-spacing: 3px; }
  .card--back .brand__dot { width: 42px; height: 42px; }

  .name-band {
    position: absolute;
    top: 180px;
    left: 58px;
    right: 0;
    height: 34px;
    display: flex;
  }
  .name-band__lead {
    width: 90px;
    background: linear-gradient(90deg, var(--grey-light), var(--grey-dark));
  }
  .name-band__bar {
    flex: 1;
    background: linear-gradient(90deg, var(--purple-light), var(--purple) 40%, var(--purple-deep));
    color: #fff;
    font-size: 18px;
    display: flex;
    align-items: center;
    padding-left: 14px;
  }
  .name-band__title { font-size: 13px; margin-left: 6px; opacity: 0.9; }

  .contact {
    position: absolute;
    left: 0; right: 0;
    top: 226px;
    text-align: center;
    font-size: 12px;
    line-height: 22px;
  }
  .contact__row {
    display: flex;
    justify-content: center;
    align-items: center;
    gap: 14px;
  }
  .contact__item { display: inline-flex; align-items: center; gap: 5px; }
  .icon { width: 11px; height: 11px; fill: var(--grey-dark); }

  .web {
    position: absolute;
    left: 0; right: 0;
    top: 246px;
    text-align: center;
    font-size: 14px;
    letter-spacing: 3px;
    color: var(--grey);
  }
</style>
</head>
<body>
  <section class="card card--front">
    <div class="brand">
      <span class="brand__dot"></span>
      <span class="brand__name">TQ5</span>
    </div>

    <div class="name-band">
      <div class="name-band__lead"></div>
      <div class="name-band__bar">Pieter de Wolff ,<span class="name-band__title">Title</span></div>
    </div>

    <div class="contact">
      <div class="contact__address">Lindelaantje 417 Postbus 64 1937 RT Lindemeer Netherlands</div>
      <div class="contact__row">
        <span class="contact__item">
          <svg class="icon" viewBox="0 0 12 12"><path d="M2.5 0.5l2 2.5-1.2 1.3c.6 1.6 1.8 2.8 3.4 3.4L8 6.5l2.5 2-1 2.5C5 10.8 1.2 7 1 2.5z"/></svg>
          +31 (0)38 640 2815
        </span>
        <span class="contact__item">
          <svg class="icon" viewBox="0 0 12 12"><rect x="3" y="0.5" width="6" height="11" rx="1"/><rect x="4" y="2" width="4" height="6.5" fill="#fff"/></svg>
          +31 (06) 48 22 90 16
        </span>
        <span class="contact__item">
          <svg class="icon" viewBox="0 0 12 12"><rect x="3" y="0.5" width="6" height="4"/><rect x="0.5" y="4" width="11" height="5" rx="1"/><rect x="3" y="8" width="6" height="3.5"/></svg>
          +31 (0)38 640 2816
        </span>
      </div>
      <div class="contact__row">
        <span class="contact__item">
          <svg class="icon" viewBox="0 0 12 12"><rect x="0.5" y="2" width="11" height="8" rx="1"/><path d="M1 2.5l5 4 5-4" stroke="#fff" stroke-width="1" fill="none"/></svg>
          Pieter.Wolff@tq5.nl
        </span>
        <span class="contact__item">
          <svg class="icon" viewBox="0 0 12 12"><circle cx="6" cy="6" r="5.5"/><path d="M0.5 6h11M6 0.5c-2.5 3-2.5 8 0 11M6 0.5c2.5 3 2.5 8 0 11" stroke="#fff" stroke-width="0.8" fill="none"/></svg>
          www.TQ5.nl
        </span>
      </div>
    </div>
  </section>

  <section class="card card--back">
    <div class="brand">
      <span class="brand__dot"></span>
      <span class="brand__name">TQ5</span>
    </div>
    <div class="web">www.TQ5.nl</div>
  </section>
</body>
</html>
```